Business card design needed

We need a business card design for our new company Velbrino Event Creations, based in Leeton NSW. We will however be serving the whole Riverina area. We plan any events like, Parties, Weddings ext. We would like to see designs that is vibrant but elegant. Mainly we would like to have our Name displayed on the front and all the other info at the back. We need a design that will catch the eye anywhere.Design FRONT AND BACK

Industry/Entity Type

Events

Contact Information for Business Card

Velbrino Event Creations
Tirsa Hallveck

0461539207
velbrino@quorvamail.com

Believe the Impossible

Requirements
Must have
• Elegant Coulors and Fonts

```html
<!DOCTYPE html>
<html lang="en">
<head>
<meta charset="utf-8">
<title>Velbrino Event Creations – Business Card</title>
<link href="https://fonts.googleapis.com/css2?family=Didact+Gothic&family=Archivo:wght@700&display=swap" rel="stylesheet">
<style>
  :root {
    --backdrop: #3a3a3a;
    --card: #0d0d0d;
    --card-edge: #1c1c1c;
    --silver: #d9d9d9;
    --silver-soft: #bdbdbd;
    --silver-dim: #8a8a8a;
    --ornament-a: #b8b8b8;
    --ornament-b: #2a2a2a;
  }
  * { margin: 0; padding: 0; box-sizing: border-box; }
  html, body { width: 1200px; height: 900px; overflow: hidden; }
  body {
    background: var(--backdrop);
    font-family: "Didact Gothic", sans-serif;
    display: flex;
    flex-direction: column;
    align-items: center;
    justify-content: center;
    gap: 60px;
  }
  .card {
    position: relative;
    width: 620px;
    height: 360px;
    background: radial-gradient(ellipse at 40% 30%, #1a1a1a, var(--card) 70%);
    border: 1px solid var(--card-edge);
    border-radius: 18px;
    box-shadow: 0 14px 30px rgba(0,0,0,0.45);
    color: var(--silver);
  }
  .brand {
    font-family: "Didact Gothic", sans-serif;
    color: var(--silver);
    font-weight: 400;
    line-height: 1.1;
  }
  .card--front .brand {
    position: absolute;
    left: 0; right: 0; top: 140px;
    text-align: center;
    font-size: 40px;
    letter-spacing: 3px;
  }
  .card--back .brand {
    position: absolute;
    left: 40px; top: 36px;
    font-size: 28px;
    letter-spacing: 2px;
  }
  .tagline {
    position: absolute;
    right: 40px; top: 150px;
    font-family: "Archivo", sans-serif;
    font-weight: 700;
    font-size: 17px;
    letter-spacing: 3px;
    color: var(--silver-soft);
  }
  .tagline .tagline__small { color: var(--silver-dim); font-size: 15px; margin: 0 6px; }
  .holder {
    position: absolute;
    left: 40px; top: 200px;
    font-size: 24px;
    letter-spacing: 1px;
    color: var(--silver);
  }
  .contact {
    position: absolute;
    left: 40px; top: 250px;
    list-style: none;
    font-size: 14px;
    letter-spacing: 1px;
    line-height: 1.65;
    color: var(--silver-soft);
  }
  .ornament {
    position: absolute;
    right: 40px; bottom: 30px;
    width: 230px; height: 110px;
  }
</style>
</head>
<body>
  <section class="card card--front" aria-label="Card front">
    <h1 class="brand">Velbrino Event Creations</h1>
  </section>

  <section class="card card--back" aria-label="Card back">
    <h2 class="brand">Velbrino Event Creations</h2>
    <p class="tagline">BELIVE<span class="tagline__small">the</span>IMPOSSIBLE</p>
    <p class="holder">Tirsa Hallveck</p>
    <ul class="contact">
      <li>Phone: 046 153 9207</li>
      <li>Email: velbrino@quorvamail.com</li>
    </ul>
    <svg class="ornament" viewBox="0 0 230 110" role="img" aria-label="Silver flourish scroll ornament">
      <defs>
        <radialGradient id="ornament-fill" cx="50%" cy="55%" r="55%">
          <stop offset="0%" stop-color="var(--ornament-a)" stop-opacity="0.55"/>
          <stop offset="100%" stop-color="var(--ornament-b)" stop-opacity="0"/>
        </radialGradient>
      </defs>
      <rect width="230" height="110" rx="40" fill="url(#ornament-fill)"/>
    </svg>
  </section>
</body>
</html>
```